Business Card and Stationary Design

After the successful redesign of our logo we are wanting to follow suite and create a new business card and stationary design!

New Logo is attached, information required on the business card should contain a mixture of the following but layout/arrangement is up to the designer.

Happy if the national provider number and abn are on the back, and happy for them to be smaller than the rest.

I am also happy to receive single sided or weird and wonderful designs.

Name
Title
National Provider Number 7291
ABN 53 219 864 317
Level 3, 42 Marlow Street
Redhill NSW 2291
Ph: 1300 987 214
Mobile: 0432 785 619
name@ferngatebuild.com.au
www.ferngatebuild.com.au

Target Market(s)

Professionals, Peers, Students, Suppliers...

Industry/Entity Type

Construction

Contact Information for Business Card

Listed in project description

Font styles to use
Other font styles liked:
• Century Gothic

Colors
0455a3
3176b5
ffffff

Requirements
Must have
• Professional Design, same color scheme as our logo
Nice to have
• Something that sets our apart from everyone else would be fantastic, open to size and shape and layout options, as long as they present professionally.
• Open to raised/embossed text, alternative materials, custom sizes, clear material
Should not have
• The color orange

```html
<!DOCTYPE html>
<html lang="en">
<head>
<meta charset="utf-8">
<title>Ferngate Build – Business Card</title>
<link rel="stylesheet" href="https://fonts.googleapis.com/css2?family=Questrial&family=Montserrat:wght@600;700&family=Open+Sans:wght@400&display=swap">
<style>
  :root {
    --stage: #e9e6e1;
    --frost-top: #f4f4f2;
    --frost-bottom: #d9dadb;
    --brand-navy: #1f2a5c;
    --brand-blue: #0455a3;
    --band-dark: #5b5b5c;
    --band-light: #8a8a8b;
    --panel-deep: #1b2456;
    --panel-mid: #2e3f82;
    --ink-light: #eef0f6;
    --ink-muted: #c9a9b0;
    --ink-soft: #d6dbea;
    --white: #ffffff;
  }
  * { margin: 0; padding: 0; box-sizing: border-box; }
  html, body { width: 1200px; height: 969px; overflow: hidden; }
  body { background: var(--stage); position: relative; }

  .card {
    position: absolute; left: 100px; top: 200px;
    width: 1000px; height: 569px;
    background: linear-gradient(180deg, var(--frost-top) 0%, var(--frost-bottom) 100%);
    border: 1px solid rgba(255,255,255,0.8);
    box-shadow: 0 18px 40px rgba(0,0,0,0.18);
    overflow: hidden;
  }

  .brand {
    position: absolute; left: 215px; top: 104px;
    display: flex; align-items: center; gap: 22px;
  }
  .brand-square { width: 86px; height: 86px; background: var(--brand-navy); }
  .brand-name {
    font-family: "Questrial", "Century Gothic", sans-serif;
    font-size: 58px; color: var(--brand-navy); letter-spacing: 0.5px;
    line-height: 1;
  }

  .name-band {
    position: absolute; left: 0; top: 326px; width: 100%; height: 66px;
    background: linear-gradient(90deg, var(--band-dark) 0%, var(--band-light) 50%, var(--band-dark) 100%);
    border-bottom: 2px solid rgba(255,255,255,0.7);
    display: flex; align-items: center; justify-content: center; gap: 12px;
    font-family: "Montserrat", sans-serif; color: var(--white);
  }
  .person-name { font-size: 31px; font-weight: 700; letter-spacing: 0.5px; }
  .person-title { font-size: 25px; font-weight: 600; letter-spacing: 0.5px; }

  .contact-panel {
    position: absolute; left: 0; top: 392px; width: 100%; height: 177px;
    background: linear-gradient(90deg, var(--panel-deep) 0%, var(--panel-mid) 55%, var(--panel-deep) 100%);
    font-family: "Open Sans", sans-serif; font-size: 24px; color: var(--ink-light);
  }
  .address-block { position: absolute; left: 43px; top: 18px; line-height: 35px; }
  .address-block .registration { color: var(--ink-muted); }
  .reach-block { position: absolute; right: 40px; top: 18px; line-height: 35px; text-align: right; }
  .reach-line { display: flex; justify-content: flex-end; align-items: center; gap: 12px; color: var(--ink-soft); }
  .reach-line svg { width: 20px; height: 20px; fill: var(--ink-soft); }
</style>
</head>
<body>
  <div class="card">
    <div class="brand">
      <div class="brand-square"></div>
      <div class="brand-name">Ferngate Build Pty Ltd</div>
    </div>

    <div class="name-band">
      <span class="person-name">DANIEL HART</span>
      <span class="person-title">- CEO/FOUNDER</span>
    </div>

    <div class="contact-panel">
      <div class="address-block">
        <div>Level 3, 42 Marlow Street</div>
        <div>Redhill NSW 2291</div>
        <div class="registration">National Provider Number 7291</div>
        <div class="registration">ABN 53 219 864 317</div>
      </div>
      <div class="reach-block">
        <div class="reach-line">1300 987 214
          <svg viewBox="0 0 20 20" aria-hidden="true"><path d="M2 7c0-3 3-4 8-4s8 1 8 4v1h-4V6H6v2H2z"/><rect x="4" y="9" width="12" height="8" rx="1"/></svg>
        </div>
        <div class="reach-line">0432 785 619
          <svg viewBox="0 0 20 20" aria-hidden="true"><path d="M6 1h8a1 1 0 0 1 1 1v16a1 1 0 0 1-1 1H6a1 1 0 0 1-1-1V2a1 1 0 0 1 1-1zm1 2v12h6V3z"/></svg>
        </div>
        <div class="reach-line">name@ferngatebuild.com.au
          <svg viewBox="0 0 20 20" aria-hidden="true"><path d="M2 5h16v10H2z M3 6l7 5 7-5" stroke="#1b2456" stroke-width="1"/></svg>
        </div>
        <div class="reach-line">www.ferngatebuild.com.au
          <svg viewBox="0 0 20 20" aria-hidden="true"><circle cx="10" cy="10" r="8"/></svg>
        </div>
      </div>
    </div>
  </div>
</body>
</html>
```